vBRIDGE ON LLC - New Website Design Help!

Need to build a website that showcases our capabilities. We will be specializing in Government Contracting for SDVOSB set aside and sole source contracts. We provide many services such as Audio & Visual design, install, consulting, all the way through to project completion. Also, IT/Voice infrastructure consulting, design, implementation, project management all the way to project completion.

Target Market(s)

IT/Voice Government Contracts, Managed Service Contracts for Government

Industry/Entity Type

Information Technology and Telecommunications

Coding

Coded - Design and coding required

Number of Pages Required

5+ page

Font styles to use
Other font styles liked:
• Calibri

Colors

Designer to choose only greyscale colors for use in the design.

Requirements
Must have
• Drop downs for additional pages, for About Us, Services, Industry Solutions, Our Company, Contact Us
Nice to have
• Testimonials page or Blog page

```html
<!DOCTYPE html>
<html lang="en">
<head>
<meta charset="utf-8">
<title>vBRIDGE ON LLC</title>
<link href="https://fonts.googleapis.com/css2?family=Fira+Sans+Condensed:wght@500;600&family=Fira+Sans:wght@500;600;700&family=Lato:ital,wght@0,400;0,700;1,400&display=swap" rel="stylesheet">
<style>
:root{
  --black:#0d0d0d;
  --ink:#1a1a1a;
  --text:#333333;
  --muted:#8a8a8a;
  --line:#4a4a4a;
  --white:#ffffff;
  --light:#e9e9e9;
  --button:#ececec;
  --footer:#1f1f1f;
  --card-line:#6a6a6a;
  --quote:#555555;
}
*{margin:0;padding:0;box-sizing:border-box}
html,body{width:1200px;height:3168px;overflow:hidden}
body{position:relative;font-family:"Lato",sans-serif;color:var(--text);background:var(--white)}
.abs{position:absolute}
h1,h2,h3,.heading{font-family:"Fira Sans",sans-serif}

/* hero */
.hero{left:0;top:0;width:1200px;height:563px;overflow:hidden}
.hero-photo{position:absolute;inset:0;background:
  radial-gradient(ellipse 380px 300px at 330px 330px,#b8582a 0%,rgba(184,88,42,0) 70%),
  radial-gradient(ellipse 300px 260px at 180px 250px,#6b5648 0%,rgba(107,86,72,0) 75%),
  linear-gradient(90deg,#5a4b40 0%,#7b6b60 35%,#6f6d6c 60%,#4a4a4c 100%)}
.hero-shade{position:absolute;inset:0;background:linear-gradient(90deg,rgba(0,0,0,0) 45%,rgba(0,0,0,.35) 100%)}
.topbar{left:0;top:0;width:1200px;height:7px;background:var(--black)}
.brand{font-family:"Fira Sans",sans-serif;font-weight:700;color:var(--white);font-size:30px;letter-spacing:1px;display:flex;align-items:center;gap:10px;white-space:nowrap}
.brand .mark{width:14px;height:14px;background:var(--white)}
.nav{left:396px;top:44px;display:flex;gap:22px;font-size:14.5px;color:var(--white);white-space:nowrap}
.nav span{display:flex;align-items:center;gap:3px}
.hero-welcome{left:689px;top:212px;color:var(--white);font-family:"Fira Sans",sans-serif;font-weight:600;font-size:35px;letter-spacing:1px;white-space:nowrap}
.hero-title{left:686px;top:276px;color:var(--white);font-family:"Fira Sans",sans-serif;font-weight:700;font-size:66px;letter-spacing:1px;line-height:1;white-space:nowrap}
.btn{display:flex;align-items:center;justify-content:center;font-weight:700;font-size:14px}
.btn-dark{left:689px;top:400px;width:125px;height:41px;background:var(--black);color:var(--white);box-shadow:3px 3px 0 var(--white)}
.btn-light{left:111px;top:982px;width:126px;height:42px;background:var(--button);color:var(--ink);box-shadow:2px 2px 0 var(--ink)}

/* about */
.about-title{left:111px;top:640px;font-size:46px;font-weight:600;color:var(--black);letter-spacing:1px}
.about-sub{left:111px;top:718px;font-size:18px;color:var(--ink)}
.about-text{left:111px;top:757px;width:495px;font-size:14.5px;line-height:28.3px;color:var(--text)}
.about-text p+p{margin-top:9px}
.about-photo{left:699px;top:647px;width:368px;height:368px;border-radius:50%;background:radial-gradient(circle at 55% 40%,#c9d2d8 0%,#8ea0ab 55%,#5d6f7a 100%)}
.badge{left:701px;top:875px;width:107px;height:133px;background:var(--white);box-shadow:0 2px 8px rgba(0,0,0,.25);padding:6px}
.badge div{width:100%;height:100%;background:#1c2b4a}

/* services */
.services{left:0;top:1119px;width:1200px;height:541px;background:linear-gradient(180deg,#1c1c1c 0%,#2a2a2a 40%,#1a1a1a 100%)}
.section-title{width:1200px;left:0;text-align:center;font-size:46px;font-weight:600;letter-spacing:1px}
.services .section-title{top:66px;color:var(--white)}
.card{top:210px;width:311px;height:232px;border:1px solid var(--card-line);background:rgba(255,255,255,.04);color:var(--white)}
.card .icon{position:absolute;left:29px;top:-33px;width:72px;height:72px;background:var(--white);display:flex;align-items:center;justify-content:center}
.card h3{position:absolute;left:29px;top:64px;font-family:"Fira Sans Condensed",sans-serif;font-size:20px;font-weight:500;white-space:nowrap;line-height:24px}
.card p{position:absolute;left:29px;top:100px;width:260px;font-size:13px;line-height:26px;color:#e4e4e4}
.arrow{width:32px;height:22px}

/* testimonials */
.testi-title{top:1738px;color:var(--black)}
.frame-back{left:121px;top:1895px;width:978px;height:278px;border:1px solid #cfcfcf}
.frame{left:113px;top:1887px;width:978px;height:278px;border:2px solid var(--line);background:var(--white)}
.quote-gap{left:540px;top:1880px;width:122px;height:12px;background:var(--white)}
.quote-circle{left:553px;top:1838px;width:96px;height:96px;border-radius:50%;background:var(--quote);display:flex;align-items:center;justify-content:center;color:var(--white);font-family:"Fira Sans",sans-serif;font-weight:700;font-size:60px;line-height:1;padding-top:22px}
.testi-text{left:135px;top:1968px;width:932px;text-align:center;font-style:italic;font-size:16px;line-height:29px;color:#555}
.testi-name{left:0;width:1200px;top:2082px;text-align:center;font-size:17px;color:var(--ink)}
.testi-place{left:0;width:1200px;top:2105px;text-align:center;font-size:14.5px;color:var(--muted)}

/* blog */
.blog{left:0;top:2266px;width:1200px;height:618px;background:var(--light)}
.blog .section-title{top:68px;color:var(--black)}
.post{top:166px;width:317px}
.post .photo{height:251px}
.post .meta{margin:22px 0 0 21px;font-size:14.5px;color:#777}
.post h3{margin:18px 0 0 21px;font-family:"Fira Sans Condensed",sans-serif;font-size:19px;font-weight:500;line-height:29px;color:var(--ink)}

/* footer */
.footer{left:0;top:2884px;width:1200px;height:284px;background:var(--footer);color:var(--white)}
.footer .brand{position:absolute;left:111px;top:52px;font-size:26px}
.cert{top:105px;width:66px;height:80px;background:var(--white);padding:4px}
.cert div{width:100%;height:100%;background:#1c2b4a}
.copy{left:116px;top:206px;font-size:14.5px;color:#cfcfcf;white-space:nowrap}
.fcol h4{font-family:"Fira Sans",sans-serif;font-weight:600;font-size:15px;letter-spacing:1px;margin-bottom:19px}
.fcol li{list-style:none;font-size:14.5px;line-height:25.5px;white-space:nowrap}
.contact li{display:flex;gap:14px;align-items:flex-start;margin-bottom:9px;line-height:25.5px}
.contact svg{flex:none;margin-top:6px}
</style>
</head>
<body>

<section class="abs hero">
  <div class="hero-photo" role="img" aria-label="Photo of three smiling colleagues gathered around a laptop in an office"></div>
  <div class="hero-shade"></div>
</section>
<div class="abs topbar"></div>
<div class="abs brand" style="left:111px;top:34px"><span class="mark"></span>vBRIDGE ON</div>
<nav class="abs nav">
  <span>About Us<svg width="9" height="6" viewBox="0 0 9 6"><path d="M1 1l3.5 3.5L8 1" fill="none" stroke="#fff" stroke-width="1.4"/></svg></span>
  <span>Services<svg width="9" height="6" viewBox="0 0 9 6"><path d="M1 1l3.5 3.5L8 1" fill="none" stroke="#fff" stroke-width="1.4"/></svg></span>
  <span>Industry Solutions<svg width="9" height="6" viewBox="0 0 9 6"><path d="M1 1l3.5 3.5L8 1" fill="none" stroke="#fff" stroke-width="1.4"/></svg></span>
  <span>Our Company<svg width="9" height="6" viewBox="0 0 9 6"><path d="M1 1l3.5 3.5L8 1" fill="none" stroke="#fff" stroke-width="1.4"/></svg></span>
  <span>Testimonials</span>
  <span>Blog</span>
  <span>Contact Us<svg width="9" height="6" viewBox="0 0 9 6"><path d="M1 1l3.5 3.5L8 1" fill="none" stroke="#fff" stroke-width="1.4"/></svg></span>
</nav>
<div class="abs hero-welcome">WELCOME TO</div>
<h1 class="abs hero-title">vBRIDGE ON</h1>
<div class="abs btn btn-dark">Learn More</div>

<h2 class="abs about-title">ABOUT US</h2>
<div class="abs about-sub">Government Contracting for SDVOSB</div>
<div class="abs about-text">
  <p>Lorem ipsum dolor sit amet, consectetur adipiscing elit, sed do eiusmd tempor incididunt ut labore et dol magna aliqua. Quis ipsum suspendisse ultrices grav ida. Risus commodo viverra maecenas accumsan lac.</p>
  <p>Sed ut perspiciatis unde omnis iste natus error sit voluptatem accusan tium doloremque laudantium, totam rem aperiam, eaque ipsa quae ab illo inventore veritatis et quasi architecto beatae vitae dicta sunt explicabo. Nemo enim ipsam voluptatem quia voluptas sit aspernatur.</p>
</div>
<div class="abs btn btn-light">Learn More</div>
<div class="abs about-photo" role="img" aria-label="Photo of two colleagues talking at a glass table in a bright office"></div>
<div class="abs badge" role="img" aria-label="Certification badge"><div></div></div>

<section class="abs services" role="img" aria-label="Darkened office photo behind the services">
  <h2 class="abs section-title">OUR SERVICES</h2>
  <svg class="abs arrow" style="left:42px;top:316px" viewBox="0 0 32 22"><path d="M30 11H3M12 2L3 11l9 9" fill="none" stroke="#777" stroke-width="2"/></svg>
  <svg class="abs arrow" style="left:1129px;top:316px" viewBox="0 0 32 22"><path d="M2 11h27M20 2l9 9-9 9" fill="none" stroke="#fff" stroke-width="2"/></svg>
  <div class="abs card" style="left:111px">
    <div class="icon"><svg width="44" height="30" viewBox="0 0 44 30" fill="none" stroke="#333" stroke-width="1.6" stroke-linecap="round"><path d="M2 15v0M7 11v8M12 7v16M17 12v6M22 2v26M27 9v12M32 5v20M37 11v8M42 15v0"/></svg></div>
    <h3>Audio &amp; Visual Design</h3>
    <p>Lorem ipsum dolor sit amet, consectetur adipiscing elit, sed do eiusod tempor inci didunt ut labore et dolore magna aliqua. Quis ipsum suspendisse ultrices.</p>
  </div>
  <div class="abs card" style="left:445px">
    <div class="icon"><svg width="44" height="44" viewBox="0 0 44 44" fill="none" stroke="#333" stroke-width="1.6" stroke-linecap="round"><rect x="16" y="4" width="12" height="22" rx="6"/><path d="M11 20a11 11 0 0 0 22 0M22 31v7M16 38h12M6 14v8M3 16v4M38 14v8M41 16v4"/></svg></div>
    <h3>Voice Infrastructure Consulting</h3>
    <p>Lorem ipsum dolor sit amet, consectetur adipiscing elit, sed do eiusod tempor inci didunt ut labore et dolore magna aliqua. Quis ipsum suspendisse ultrices.</p>
  </div>
  <div class="abs card" style="left:778px">
    <div class="icon"><svg width="44" height="44" viewBox="0 0 44 44" fill="none" stroke="#333" stroke-width="1.6"><circle cx="22" cy="22" r="13"/><circle cx="22" cy="22" r="6"/><path d="M22 3v6M22 35v6M3 22h6M35 22h6M8.5 8.5l4 4M31.5 31.5l4 4M8.5 35.5l4-4M31.5 12.5l4-4"/></svg></div>
    <h3>Project Management</h3>
    <p>Lorem ipsum dolor sit amet, consectetur adipiscing elit, sed do eiusod tempor inci didunt ut labore et dolore magna aliqua. Quis ipsum suspendisse ultrices.</p>
  </div>
</section>

<h2 class="abs section-title testi-title">CLIENT TESTIMONIALS</h2>
<div class="abs frame-back"></div>
<div class="abs frame"></div>
<div class="abs quote-gap"></div>
<div class="abs quote-circle">&ldquo;</div>
<svg class="abs arrow" style="left:40px;top:1995px" viewBox="0 0 32 22"><path d="M30 11H3M12 2L3 11l9 9" fill="none" stroke="#bbb" stroke-width="2"/></svg>
<svg class="abs arrow" style="left:1128px;top:1995px" viewBox="0 0 32 22"><path d="M2 11h27M20 2l9 9-9 9" fill="none" stroke="#555" stroke-width="2"/></svg>
<p class="abs testi-text">Lorem ipsum dolor sit amet, consectetur adipiscing elit, sed do eiusmod tempor incididunt ut labore et dolore magna aliqua. Ut enim ad minim veniam, quis nostrud exercitation ullamco laboris nisi ut aliquip ex ea commodo consequat. Duis aute irure dolor in repre henderit in voluptate velit esse cillum dolore eu fugiat nulla pariatur.</p>
<div class="abs testi-name">Marla Quentin</div>
<div class="abs testi-place">Newyork</div>

<section class="abs blog">
  <h2 class="abs section-title">LATEST BLOG</h2>
  <article class="abs post" style="left:111px">
    <div class="photo" role="img" aria-label="Photo of a woman on the phone working at a laptop" style="background:linear-gradient(135deg,#d9d9d9,#8f8f8f 60%,#5e5e5e)"></div>
    <div class="meta">By admin | February 23, 2024</div>
    <h3>Excepteur sint occaecat cupidatat non proident, sunt</h3>
  </article>
  <article class="abs post" style="left:443px">
    <div class="photo" role="img" aria-label="Photo of two smiling colleagues in a bright office" style="background:linear-gradient(135deg,#eaeaea,#a9a59f 55%,#3d4a44)"></div>
    <div class="meta">By admin | February 23, 2024</div>
    <h3>Excepteur sint occaecat cupidatat non proident, sunt</h3>
  </article>
  <article class="abs post" style="left:772px">
    <div class="photo" role="img" aria-label="Photo of a team reviewing work on a desktop monitor" style="background:linear-gradient(135deg,#bcbcbc,#6f6a66 55%,#3a3a40)"></div>
    <div class="meta">By admin | February 23, 2024</div>
    <h3>Excepteur sint occaecat cupidatat non proident, sunt</h3>
  </article>
</section>

<footer class="abs footer">
  <div class="brand"><span class="mark"></span>vBRIDGE ON</div>
  <div class="abs cert" style="left:113px" role="img" aria-label="Certification badge"><div></div></div>
  <div class="abs cert" style="left:191px" role="img" aria-label="Certification badge"><div></div></div>
  <div class="abs copy">2024 vBridge On. All Rights Reserved.</div>
  <div class="abs fcol" style="left:424px;top:70px">
    <h4>QUICK LINKS</h4>
    <ul><li>About Us</li><li>Services</li><li>Industry Solutions</li><li>Our Company</li></ul>
  </div>
  <div class="abs fcol" style="left:646px;top:70px">
    <h4>OTHER LINKS</h4>
    <ul><li>Testimonials</li><li>Blog</li><li>Contact Us</li><li>Terms &amp; Conditions</li></ul>
  </div>
  <div class="abs fcol contact" style="left:887px;top:70px">
    <h4>CONTACT US</h4>
    <ul>
      <li><svg width="14" height="18" viewBox="0 0 14 18"><path d="M7 0a7 7 0 0 0-7 7c0 5 7 11 7 11s7-6 7-11a7 7 0 0 0-7-7z" fill="#fff"/><circle cx="7" cy="7" r="2.6" fill="#1f1f1f"/></svg><span>vBridge On,<br>Address Comes Here</span></li>
      <li><svg width="15" height="15" viewBox="0 0 15 15"><path d="M3.2 0.5l2.4 3-1.4 1.8c.9 2 2.5 3.6 4.5 4.5l1.8-1.4 3 2.4-1.3 2.6C7 13.6 1.4 8 .6 1.8z" fill="#fff"/></svg><span>Phone: +1-800-555-0147</span></li>
      <li><svg width="15" height="12" viewBox="0 0 15 12"><rect width="15" height="12" rx="1" fill="#fff"/><path d="M1 1.5l6.5 5 6.5-5" fill="none" stroke="#1f1f1f" stroke-width="1.3"/></svg><span>admin@vbridgeon.com</span></li>
    </ul>
  </div>
</footer>

</body>
</html>
```